New website for Pollard Law Firm at www.keepwinning-example.com

We are a professional law firm located in the Nashville, Tennessee USA area. We focus on personal injury law. We are looking for a slick new website that is user friendly for updating with new blogs, videos, etc. The primary colors should be red, black, and white. It should load extremely fast and have a good mobile component. The pages for the design will include a home page, about us, news, contact us, and practice page. The practice page will be copied for all the practice areas including motor vehicle accidents, slip and fall accidents, dog bites, etc. We have included an image which we would like to include in the new site which shows the color scheme The image is called banner-Car Wreck. The new website should NOT have gavels, court houses, law books, scales or the typical images for a law firm.

Target Market(s)

People in Tennessee involved in accidents

Industry/Entity Type

Legal services, law firm

Coding

Coded - Design and coding required

Number of Pages Required

5+ page

Font styles to use
Serif

Colors
EB3D1F
EC4F4E
F09395
F8D3D4
FCEDEE

Requirements
Should not have
• Gavels, columns, scales, law related images

```html
<!DOCTYPE html>
<html lang="en">
<head>
<meta charset="utf-8">
<title>Pollard Law Firm PLLC</title>
<link href="https://fonts.googleapis.com/css2?family=Rubik:wght@400;500;700&family=Roboto:ital,wght@0,400;0,500;0,700;1,400;1,700&display=swap" rel="stylesheet">
<style>
:root{
  --red:#c4191f;
  --red-bright:#d42a2a;
  --red-dark:#a3170f;
  --red-deep:#951c12;
  --black:#0b0b0b;
  --ink:#141414;
  --muted:#6b6b6b;
  --soft:#f5f6f8;
  --line:#ececec;
  --tag-bg:#e3f4ea;
  --tag-ink:#2f9e62;
  --white:#ffffff;
}
*{margin:0;padding:0;box-sizing:border-box}
html,body{width:1200px;height:3690px;overflow:hidden}
body{font-family:"Roboto",sans-serif;color:var(--ink);background:var(--white);position:relative}
.abs{position:absolute}
h1,h2,h3,h4{font-family:"Rubik",sans-serif}

/* top bar */
.topbar{top:0;left:0;width:1200px;height:50px;background:var(--red);color:#fff;font-size:12px}
.topbar .contact{left:159px;top:17px;display:flex;gap:22px;align-items:center}
.topbar .contact span{display:flex;align-items:center;gap:8px}
.topbar .social{left:952px;top:19px;display:flex;gap:12px}
.topbar .social i{width:10px;height:10px;border-radius:50%;background:#fff;display:block}

/* nav */
.nav{top:50px;left:0;width:1200px;height:96px;background:#fff}
.brand{left:159px;top:26px;color:var(--red);font-family:"Rubik",sans-serif;font-weight:500;line-height:1}
.brand .name{font-size:22px;letter-spacing:1px}
.brand .sub{font-size:11px;letter-spacing:2px;margin-top:3px;padding-left:24px}
.menu{left:701px;top:14px;display:flex;gap:32px;font-size:10px;font-weight:500;color:var(--red);letter-spacing:.4px}
.menu a{color:inherit;text-decoration:none;position:relative}
.menu a.active::after{content:"";position:absolute;left:9px;right:9px;top:17px;height:2px;background:var(--red)}

/* hero */
.hero{top:146px;left:0;width:1200px;height:447px;background:var(--black)}
.hero .photo{left:560px;top:0;width:640px;height:447px;background:radial-gradient(ellipse at 55% 55%,#b3121c 0%,#6d0b10 35%,#1b0c0e 70%,#0b0b0b 100%)}
.hero .badge{left:173px;top:100px;background:var(--red);color:#fff;font-size:9px;letter-spacing:2.5px;font-weight:500;padding:9px 14px}
.hero h1{left:173px;top:140px;color:var(--red-bright);font-size:38px;line-height:57px;font-weight:500}
.hero p{left:173px;top:262px;color:#fff;font-size:12.5px}

/* tags and headings */
.tag{background:var(--tag-bg);color:var(--tag-ink);font-size:9px;font-weight:700;letter-spacing:2.6px;padding:9px 14px}
.center{left:0;width:1200px;text-align:center}
.title{font-size:37px;font-weight:500;color:var(--black)}
.title em{font-style:normal;color:var(--red)}
.divider{left:562px;width:76px;height:6px;display:flex;gap:4px}
.divider i{display:block;height:6px;border-radius:3px;background:#e4ebe8;flex:1}
.divider i.mid{background:var(--red);flex:1.6}
.lead{font-size:12.5px;line-height:24px;color:var(--red)}
.lead.grey{color:var(--muted)}

/* about */
.about{top:593px;left:0;width:1200px;height:535px;background:linear-gradient(180deg,#fafbfc,#f1f3f6)}
.about h2{left:159px;top:120px;font-size:31px;font-weight:500}
.about .text{left:159px;top:177px;width:420px;font-size:12px;line-height:24px;color:var(--red)}
.quote{left:159px;top:266px;width:428px;height:123px;background:#fff;border-left:3px solid var(--tag-ink);padding:24px 0 0 24px;box-shadow:0 10px 30px rgba(0,0,0,.06)}
.quote p{font-size:12px;font-style:italic;line-height:24px;color:var(--red)}
.quote b{display:block;margin-top:5px;font-size:12px;font-style:italic;color:var(--ink)}
.btn{display:flex;align-items:center;background:var(--red);color:#fff;font-size:12px;font-weight:500}
.btn .lbl{flex:1;padding-left:24px}
.btn .arr{height:100%;display:flex;align-items:center;justify-content:center;border-left:1px solid rgba(255,255,255,.35)}
.about .btn{left:159px;top:415px;width:156px;height:46px}
.about .btn .arr{width:46px}
.video{left:611px;top:103px;width:430px;height:286px;background:linear-gradient(135deg,#58636b,#8c9aa2 45%,#c9d3d6 70%,#6f7b80)}
.video .play{left:184px;top:112px;width:62px;height:62px;border-radius:50%;background:var(--red);display:flex;align-items:center;justify-content:center}

/* services */
.card{background:#fff;box-shadow:0 6px 24px rgba(0,0,0,.08)}
.svc{top:1372px;width:272px;height:315px}
.svc .img{height:163px}
.svc h3{position:absolute;left:23px;top:191px;font-size:13.5px;font-weight:700;color:var(--red)}
.svc p{position:absolute;left:23px;top:215px;width:232px;font-size:8.5px;line-height:17px;color:var(--muted);text-transform:uppercase}
.small-btn{position:absolute;height:29px;width:115px}
.small-btn .lbl{padding-left:15px;font-size:10.5px}
.small-btn .arr{width:32px}
.svc .small-btn{left:23px;top:263px}

/* contact */
.map{left:169px;top:2010px;width:347px;height:390px;background:linear-gradient(135deg,#e9ece4 0%,#dfe6d6 45%,#b7d3ee 70%,#a8c9ea 100%)}
.field{background:#fff;box-shadow:0 4px 18px rgba(0,0,0,.06);display:flex;align-items:flex-start;gap:10px;padding:16px 16px;font-size:11.5px;color:var(--muted)}
.field svg{flex:none}
.field .chev{margin-left:auto;width:22px;height:22px;border-radius:50%;background:var(--tag-bg);display:flex;align-items:center;justify-content:center;margin-top:-3px}
.send{left:540px;top:2374px;width:129px;height:46px;background:var(--red);color:#fff;font-size:12px;font-weight:500;display:flex;align-items:center;justify-content:center}

/* news */
.strip{left:105px;top:2814px;width:990px;height:410px;background:#fff;box-shadow:0 0 40px rgba(0,0,0,.04)}
.post{top:2832px;width:273px;height:383px}
.post .img{height:182px;background:linear-gradient(135deg,#3c4650,#8e9aa3 45%,#d7dde1 65%,#5a646b)}
.post .meta{position:absolute;left:23px;top:208px;display:flex;gap:14px;font-size:11px;color:var(--muted)}
.post .meta span{display:flex;align-items:center;gap:6px}
.post h4{position:absolute;left:23px;top:239px;font-size:15px;font-weight:500}
.post p{position:absolute;left:23px;top:268px;width:230px;font-size:11.5px;line-height:24px;color:var(--muted)}
.post .small-btn{left:23px;top:331px}

/* footer */
.footer{top:3295px;left:0;width:1200px;height:324px;background:var(--red-dark);color:#fff}
.footer h4{position:absolute;top:65px;font-size:18.5px;font-weight:500}
.footer .about-txt{left:159px;top:111px;width:175px;font-size:12px;line-height:25px}
.footer .socials{left:159px;top:217px;display:flex;gap:9px}
.footer .socials i{display:block;width:39px;height:39px;border:1px solid rgba(255,255,255,.25);background:rgba(255,255,255,.06)}
.links{top:106px;list-style:none;font-size:12px}
.links li{display:flex;align-items:center;gap:16px;height:27px}
.footer .nl-txt{left:839px;top:113px;font-size:12px}
.footer .input{left:839px;top:165px;width:202px;height:39px;background:rgba(255,255,255,.12);font-size:12px;color:rgba(255,255,255,.6);padding:13px 16px}
.footer .subscribe{left:839px;top:218px;width:202px;height:37px;background:var(--red-bright)}
.footer .subscribe .lbl{padding-left:0;text-align:center}
.footer .subscribe .arr{width:37px;border-left:0;background:rgba(0,0,0,.08)}
.bottom{top:3619px;left:0;width:1200px;height:71px;background:var(--red-deep);color:#fff;font-size:12px;padding:35px 0 0 159px}
</style>
</head>
<body>

<header>
  <div class="abs topbar">
    <div class="abs contact">
      <span><svg width="11" height="9" viewBox="0 0 11 9"><rect x="0.5" y="0.5" width="10" height="8" fill="none" stroke="#fff"/><path d="M0.5 0.5 5.5 5 10.5 0.5" fill="none" stroke="#fff"/></svg>office@pollardlawfirm-example.com</span>
      <span><svg width="10" height="10" viewBox="0 0 10 10"><path d="M2 0.5 4 3 3 4.2Q4.5 6.5 5.8 7L7 6l2.5 2-1 1.5Q4.5 10 0.5 2.5Z" fill="#fff"/></svg>(615) 555-0148</span>
    </div>
    <div class="abs social"><i></i><i></i><i></i><i></i></div>
  </div>
  <nav class="abs nav">
    <div class="abs brand"><div class="name">POLLARD</div><div class="sub">LAW FIRM PLLC</div></div>
    <div class="abs menu" style="top:14px;padding-top:0">
      <div style="position:relative;top:0;display:flex;gap:32px;margin-top:-14px;padding-top:0"></div>
    </div>
    <div class="abs menu" style="top:14px;left:701px;margin-top:0;">
      <a class="active" href="#" style="margin-top:0;top:0;position:relative;line-height:10px;transform:translateY(0);display:block;padding-top:0;">HOME</a>
      <a href="#" style="line-height:10px">PRACTICE</a>
      <a href="#" style="line-height:10px">ABOUT US</a>
      <a href="#" style="line-height:10px">NEWS</a>
      <a href="#" style="line-height:10px">CONTACT</a>
    </div>
  </nav>
</header>

<section class="abs hero">
  <div class="abs photo" role="img" aria-label="Red car crashing with shattered windshield glass"></div>
  <div class="abs badge">POLLARD LAW FIRM PLLC</div>
  <h1 class="abs">Don't Lose What Is<br>Legally Yours</h1>
  <p class="abs">Lorem Ipsum Dolor Sit Amet Dummy Text For Web Development And Design</p>
</section>

<section class="abs about">
  <div class="abs tag" style="left:159px;top:80px">WHO WE ARE</div>
  <h2 class="abs">Lorem Ipsum Dolor Title</h2>
  <p class="abs text">Lorem ipsum dolor sit amet, consectetur adipiscing elit, sed do eiusmod tempor incididunt ut labore et dolore magna aliqua. Ut enim ad minim veniam, quis nostrud exercitation ullamco laboris nisi ut aliquip</p>
  <div class="abs quote">
    <p>Lorem ipsum dolor sit amet, consectetur adipiscing elit, sed do eiusmod tempor incididunt ut labore et dolore magna aliqua.</p>
    <b>Lorem Ipsum Dolor</b>
  </div>
  <div class="abs btn"><span class="lbl">Read More</span><span class="arr"><svg width="12" height="10" viewBox="0 0 12 10"><path d="M0 5h10M6 1l4 4-4 4" fill="none" stroke="#fff" stroke-width="1.8"/></svg></span></div>
  <div class="abs video" role="img" aria-label="Insurance adjuster writing on a clipboard beside a damaged car">
    <div class="abs play"><svg width="14" height="16" viewBox="0 0 14 16"><path d="M2 1l11 7-11 7z" fill="#fff"/></svg></div>
  </div>
</section>

<section>
  <div class="abs center" style="top:1162px"><span class="tag" style="display:inline-block">WHAT WE DO</span></div>
  <h2 class="abs center title" style="top:1201px">Our <em>Services</em></h2>
  <div class="abs divider" style="top:1259px"><i></i><i class="mid"></i><i></i></div>
  <p class="abs center lead" style="top:1282px">It is a long established fact that a reader will be distracted by the readable content of a<br>page when looking at its layout.</p>

  <article class="abs card svc" style="left:168px">
    <div class="img" role="img" aria-label="Paramedic helping an injured person after a car accident" style="background:linear-gradient(135deg,#b3151a,#d6403a 40%,#6a6e72 70%,#2c2f33)"></div>
    <h3>PERSONAL INJURY</h3>
    <p>Don't lose the money which the insurance company is trying to keep from you</p>
    <div class="btn small-btn"><span class="lbl">Read More</span><span class="arr"><svg width="10" height="9" viewBox="0 0 12 10"><path d="M0 5h10M6 1l4 4-4 4" fill="none" stroke="#fff" stroke-width="2"/></svg></span></div>
  </article>
  <article class="abs card svc" style="left:464px">
    <div class="img" role="img" aria-label="Professionals in a business meeting" style="background:linear-gradient(135deg,#d8dde2,#a9b4bf 40%,#2b3443 75%,#1b2230)"></div>
    <h3>PROFESSIONAL LICENSES</h3>
    <p>Don't lose your license which the state is trying to take away from you</p>
    <div class="btn small-btn"><span class="lbl">Read More</span><span class="arr"><svg width="10" height="9" viewBox="0 0 12 10"><path d="M0 5h10M6 1l4 4-4 4" fill="none" stroke="#fff" stroke-width="2"/></svg></span></div>
  </article>
  <article class="abs card svc" style="left:760px">
    <div class="img" role="img" aria-label="Family with a young child talking with an advisor" style="background:linear-gradient(135deg,#6b4a3a,#c9a58c 40%,#ece5df 65%,#3a3f4a)"></div>
    <h3>CHILD CUSTODY</h3>
    <p>Don't lose your family who you would give anything to keep</p>
    <div class="btn small-btn"><span class="lbl">Read More</span><span class="arr"><svg width="10" height="9" viewBox="0 0 12 10"><path d="M0 5h10M6 1l4 4-4 4" fill="none" stroke="#fff" stroke-width="2"/></svg></span></div>
  </article>
</section>

<section>
  <div class="abs center" style="top:1797px"><span class="tag" style="display:inline-block">CONTACT US</span></div>
  <h2 class="abs center title" style="top:1836px">Get In <em>Touch</em></h2>
  <div class="abs divider" style="top:1894px"><i></i><i class="mid"></i><i></i></div>
  <p class="abs center lead grey" style="top:1917px">It is a long established fact that a reader will be distracted by the readable content of a<br>page when looking at its layout.</p>

  <div class="abs map" role="img" aria-label="Map showing the office location"></div>

  <div class="abs field" style="left:540px;top:2010px;width:236px;height:48px"><svg width="12" height="12" viewBox="0 0 12 12"><circle cx="6" cy="3.5" r="2.8" fill="none" stroke="#c4191f" stroke-width="1.2"/><path d="M1 11.5q5-7 10 0" fill="none" stroke="#c4191f" stroke-width="1.2"/></svg>Your Full Name *</div>
  <div class="abs field" style="left:799px;top:2010px;width:236px;height:48px"><svg width="12" height="10" viewBox="0 0 12 10"><rect x="0.6" y="0.6" width="10.8" height="8.8" fill="none" stroke="#c4191f" stroke-width="1.2"/><path d="M0.6 0.6 6 5l5.4-4.4" fill="none" stroke="#c4191f" stroke-width="1.2"/></svg>Your Email *</div>
  <div class="abs field" style="left:540px;top:2082px;width:236px;height:46px"><svg width="9" height="12" viewBox="0 0 9 12"><rect x="0.6" y="0.6" width="7.8" height="10.8" rx="1" fill="none" stroke="#c4191f" stroke-width="1.2"/><rect x="3" y="9" width="3" height="1" fill="#c4191f"/></svg>Your Phone *</div>
  <div class="abs field" style="left:799px;top:2082px;width:236px;height:46px"><svg width="12" height="12" viewBox="0 0 12 12"><circle cx="6" cy="3.5" r="2.8" fill="none" stroke="#c4191f" stroke-width="1.2"/><path d="M1 11.5q5-7 10 0" fill="none" stroke="#c4191f" stroke-width="1.2"/></svg>Please Select<span class="chev"><svg width="8" height="5" viewBox="0 0 8 5"><path d="M0.5 0.5 4 4l3.5-3.5" fill="none" stroke="#2f9e62" stroke-width="1.2"/></svg></span></div>
  <div class="abs field" style="left:540px;top:2152px;width:495px;height:198px"><svg width="12" height="12" viewBox="0 0 12 12"><path d="M0.6 5 6 0.8 11.4 5v6.4H0.6z" fill="none" stroke="#c4191f" stroke-width="1.2"/><path d="M0.6 5 6 8.5 11.4 5" fill="none" stroke="#c4191f" stroke-width="1.2"/></svg>Your Message *</div>
  <div class="abs send">Send Message</div>
</section>

<section>
  <div class="abs center" style="top:2582px"><span class="tag" style="display:inline-block">NEWS</span></div>
  <h2 class="abs center title" style="top:2627px;font-size:39px">What's <em>Happening Around</em></h2>
  <div class="abs divider" style="top:2688px"><i></i><i class="mid"></i><i></i></div>
  <p class="abs center lead" style="top:2714px;font-size:13.5px;line-height:26px">It is a long established fact that a reader will be distracted by the readable content of a<br>page when looking at its layout.</p>
  <div class="abs strip"></div>

  <article class="abs card post" style="left:178px">
    <div class="img" role="img" aria-label="Person filling in an accident report beside a damaged car"></div>
    <div class="meta"><span><svg width="10" height="10" viewBox="0 0 10 10"><rect x="0.6" y="1.6" width="8.8" height="7.8" fill="none" stroke="#c4191f" stroke-width="1.2"/><path d="M0.6 4h8.8" stroke="#c4191f" stroke-width="1.2"/></svg>10 March</span><span><svg width="8" height="10" viewBox="0 0 8 10"><path d="M0.6 0.6h6.8v8.8L4 7 0.6 9.4z" fill="none" stroke="#c4191f" stroke-width="1.2"/></svg>Business</span></div>
    <h4>Lorem Ipsum Dolor Sit</h4>
    <p>It is a long established fact that a reader will be distracted..</p>
    <div class="btn small-btn"><span class="lbl">Read More</span><span class="arr"><svg width="10" height="9" viewBox="0 0 12 10"><path d="M0 5h10M6 1l4 4-4 4" fill="none" stroke="#fff" stroke-width="2"/></svg></span></div>
  </article>
  <article class="abs card post" style="left:474px">
    <div class="img" role="img" aria-label="Person filling in an accident report beside a damaged car"></div>
    <div class="meta"><span><svg width="10" height="10" viewBox="0 0 10 10"><rect x="0.6" y="1.6" width="8.8" height="7.8" fill="none" stroke="#c4191f" stroke-width="1.2"/><path d="M0.6 4h8.8" stroke="#c4191f" stroke-width="1.2"/></svg>10 August</span><span><svg width="8" height="10" viewBox="0 0 8 10"><path d="M0.6 0.6h6.8v8.8L4 7 0.6 9.4z" fill="none" stroke="#c4191f" stroke-width="1.2"/></svg>Business</span></div>
    <h4>Lorem Ipsum Dolor Sit</h4>
    <p>It is a long established fact that a reader will be distracted..</p>
    <div class="btn small-btn"><span class="lbl">Read More</span><span class="arr"><svg width="10" height="9" viewBox="0 0 12 10"><path d="M0 5h10M6 1l4 4-4 4" fill="none" stroke="#fff" stroke-width="2"/></svg></span></div>
  </article>
  <article class="abs card post" style="left:772px">
    <div class="img" role="img" aria-label="Person filling in an accident report beside a damaged car"></div>
    <div class="meta"><span><svg width="10" height="10" viewBox="0 0 10 10"><rect x="0.6" y="1.6" width="8.8" height="7.8" fill="none" stroke="#c4191f" stroke-width="1.2"/><path d="M0.6 4h8.8" stroke="#c4191f" stroke-width="1.2"/></svg>13 July</span><span><svg width="10" height="10" viewBox="0 0 10 10"><path d="M0.6 0.6h4.5l4.3 4.3-4.5 4.5L0.6 5.1z" fill="#c4191f"/></svg>Business</span></div>
    <h4>Lorem Ipsum Dolor Sit</h4>
    <p>It is a long established fact that a reader will be distracted..</p>
    <div class="btn small-btn"><span class="lbl">Read More</span><span class="arr"><svg width="10" height="9" viewBox="0 0 12 10"><path d="M0 5h10M6 1l4 4-4 4" fill="none" stroke="#fff" stroke-width="2"/></svg></span></div>
  </article>
</section>

<footer class="abs footer">
  <h4 style="left:159px">About Us</h4>
  <p class="abs about-txt">Lorem, ipsum dolor sit amet Lorem, ipsum dolor sit amet consectetur adipisicing elit.</p>
  <div class="abs socials"><i></i><i></i><i></i><i></i></div>

  <h4 style="left:385px">Usefull Links</h4>
  <ul class="abs links" style="left:385px">
    <li><svg width="11" height="9" viewBox="0 0 12 10"><path d="M0 5h10M6 1l4 4-4 4" fill="none" stroke="#fff" stroke-width="1.8"/></svg>Home</li>
    <li><svg width="11" height="9" viewBox="0 0 12 10"><path d="M0 5h10M6 1l4 4-4 4" fill="none" stroke="#fff" stroke-width="1.8"/></svg>About</li>
    <li><svg width="11" height="9" viewBox="0 0 12 10"><path d="M0 5h10M6 1l4 4-4 4" fill="none" stroke="#fff" stroke-width="1.8"/></svg>Practice</li>
    <li><svg width="11" height="9" viewBox="0 0 12 10"><path d="M0 5h10M6 1l4 4-4 4" fill="none" stroke="#fff" stroke-width="1.8"/></svg>News</li>
    <li><svg width="11" height="9" viewBox="0 0 12 10"><path d="M0 5h10M6 1l4 4-4 4" fill="none" stroke="#fff" stroke-width="1.8"/></svg>Contact</li>
  </ul>

  <h4 style="left:611px">Help Links</h4>
  <ul class="abs links" style="left:611px">
    <li><svg width="11" height="9" viewBox="0 0 12 10"><path d="M0 5h10M6 1l4 4-4 4" fill="none" stroke="#fff" stroke-width="1.8"/></svg>Team Details</li>
    <li><svg width="11" height="9" viewBox="0 0 12 10"><path d="M0 5h10M6 1l4 4-4 4" fill="none" stroke="#fff" stroke-width="1.8"/></svg>Privacy Policy</li>
    <li><svg width="11" height="9" viewBox="0 0 12 10"><path d="M0 5h10M6 1l4 4-4 4" fill="none" stroke="#fff" stroke-width="1.8"/></svg>Cookies Policy</li>
    <li><svg width="11" height="9" viewBox="0 0 12 10"><path d="M0 5h10M6 1l4 4-4 4" fill="none" stroke="#fff" stroke-width="1.8"/></svg>Supports Center</li>
    <li><svg width="11" height="9" viewBox="0 0 12 10"><path d="M0 5h10M6 1l4 4-4 4" fill="none" stroke="#fff" stroke-width="1.8"/></svg>Terms &amp; Conditions</li>
  </ul>

  <h4 style="left:839px">Newsletter</h4>
  <p class="abs nl-txt">Lorem, ipsum dolor sit amet</p>
  <div class="abs input">E-mail</div>
  <div class="abs btn subscribe"><span class="lbl">Subscribe</span><span class="arr"><svg width="12" height="10" viewBox="0 0 12 10"><path d="M0 5h10M6 1l4 4-4 4" fill="none" stroke="#fff" stroke-width="1.8"/></svg></span></div>
</footer>
<div class="abs bottom">© 2022 All Right Reserved</div>

</body>
</html>
```